Coral Pillow Depot Website

Need a design for a local Miami mattress store.
The store is called Coral Pillow Depot.
need it to be something that customers can find on the internet and will
give them my location, they need to know i have the same brand mattress as the other store except i have them at almost half the price.

the office phone number is (786)555-0147
the office address is: 4721 sw Heron Glade Ave, Miami FL 33190

included is the logo, id like to stick the with white and teal design

here are is an excerpt that can or cannot be included

"We are a premium mattress discount outlet store located in South Florida; offering Free Delivery to Broward Miami-Dade, the Keys, and Palm Beach.

We carry the best brands in the market: Harlow DreamNest; Brovik SpineEase, Kendal & Pryce, Tarvin, among others.

We are open 7 days a week, and we are accessible from all major highways. We are a family business and our goal is to provide you with the most comfortable and best quality mattress at a price that has no competition. Come visit us and take a look at our large inventory selection."

```html
<!DOCTYPE html>
<html lang="en">
<head>
<meta charset="utf-8">
<title>Coral Pillow Depot</title>
<link rel="stylesheet" href="https://fonts.googleapis.com/css2?family=Arimo&family=Sorts+Mill+Goudy&display=swap">
<style>
  :root {
    --backdrop: #c4c4c4;
    --page: #ebebea;
    --teal: #1ea9c9;
    --ink: #111111;
    --body-ink: #2a2a2a;
    --footer: #000000;
    --footer-ink: #ffffff;
    --mattress-mid: #d9dbe0;
    --mattress-blue: #a9b6cc;
  }
  * { margin: 0; padding: 0; box-sizing: border-box; }
  html, body { width: 1200px; height: 890px; overflow: hidden; }
  body { background: var(--backdrop); position: relative; font-family: "Arimo", Arial, sans-serif; }

  .page {
    position: absolute; left: 116px; top: 2px; width: 962px; height: 888px;
    background: var(--page); border: 2px solid #ffffff; border-bottom: none;
  }

  .brand {
    position: absolute; left: 0; top: 62px; width: 958px; text-align: center;
    font-family: "Sorts Mill Goudy", Georgia, serif; font-size: 40px; color: #3a3a3a;
    letter-spacing: 0.5px;
  }

  .main-nav {
    position: absolute; left: 0; top: 148px; width: 958px; height: 38px;
    border-top: 2px solid var(--teal); border-bottom: 2px solid var(--teal);
  }
  .main-nav a {
    position: absolute; top: 7px; transform: translateX(-50%);
    font-size: 19px; color: var(--ink); text-decoration: none; letter-spacing: 0.3px;
  }

  .headline {
    position: absolute; left: 45px; top: 280px;
    font-family: "Sorts Mill Goudy", Georgia, serif; font-weight: 400;
    font-size: 50px; line-height: 55px; color: var(--ink); letter-spacing: 3px;
    white-space: nowrap;
  }
  .headline span { display: block; }
  .headline .indent { padding-left: 112px; letter-spacing: 3.6px; }

  .about {
    position: absolute; left: 609px; top: 231px; width: 310px; height: 330px;
    border-left: 2px solid var(--teal); padding-left: 21px;
  }
  .about h2 { font-weight: 400; font-size: 24px; color: var(--ink); margin-top: 8px; letter-spacing: 0.3px; }
  .about p {
    margin-top: 28px; width: 282px; font-family: "Sorts Mill Goudy", Georgia, serif;
    font-size: 13.6px; line-height: 17.4px; color: var(--body-ink);
    text-align: justify; hyphens: auto; height: 262px; overflow: hidden;
  }

  .product { position: absolute; top: 616px; width: 273px; height: 111px; }
  .product--blue { left: 41px; background: linear-gradient(180deg, #f6f7f9 0%, var(--mattress-mid) 45%, var(--mattress-blue) 100%); }
  .product--cream { left: 340px; background: linear-gradient(180deg, #fbfaf6 0%, #ece8dc 55%, #d7d2c2 100%); }
  .product--white { left: 639px; background: linear-gradient(180deg, #ffffff 0%, #e7e9ee 55%, #cfd3da 100%); }

  .contact-icons { position: absolute; left: 752px; top: 771px; }

  .site-footer {
    position: absolute; left: 0; top: 808px; width: 958px; height: 80px;
    background: var(--footer); color: var(--footer-ink); font-size: 11px; line-height: 13px;
  }
  .site-footer .col { position: absolute; top: 11px; white-space: nowrap; }
  .site-footer .legal { left: 10px; }
  .site-footer .social { left: 343px; }
  .site-footer .helpline { left: 620px; }
  .thumb { position: absolute; top: 35px; height: 30px; background: linear-gradient(180deg, #f2f2f2, #b9bbbf); }
</style>
</head>
<body>
  <div class="page">
    <header>
      <div class="brand">Coral Pillow Depot</div>
      <nav class="main-nav">
        <a href="#" style="left:125px">About</a>
        <a href="#" style="left:359px">Matress</a>
        <a href="#" style="left:593px;top:5px">Shop</a>
        <a href="#" style="left:827px">Contact</a>
      </nav>
    </header>

    <h1 class="headline"><span>We sell matresses</span><span class="indent">at the best prices</span></h1>

    <section class="about">
      <h2>About us</h2>
      <p>We are a premium mattress discount outlet store located in South Florida, offering Free Delivery to Broward, Miami-Dade, the Keys and Palm Beach. We carry the same brands as the other stores at almost half the price: Harlow DreamNest, Brovik SpineEase, Kendal &amp; Pryce, Tarvin, among others. We are open 7 days a week and accessible from all major highways. Visit us at 4721 sw Heron Glade Ave, Miami FL 33190 or call (786)555-0147. We are a family business and our goal is to give you the most comfortable, best quality mattress at a price with no competition.</p>
    </section>

    <div class="product product--blue" role="img" aria-label="Photo of a blue quilted mattress on a box spring"></div>
    <div class="product product--cream" role="img" aria-label="Photo of a cream pillow-top mattress"></div>
    <div class="product product--white" role="img" aria-label="Photo of a white quilted pillow-top mattress"></div>

    <svg class="contact-icons" width="200" height="30" viewBox="0 0 200 30" aria-label="Contact icons">
      <g fill="var(--teal)">
        <circle cx="14" cy="15" r="14"/><circle cx="47" cy="15" r="14"/><circle cx="80" cy="15" r="14"/>
        <circle cx="113" cy="15" r="14"/><circle cx="147" cy="15" r="14"/><circle cx="180" cy="15" r="14"/>
      </g>
      <g fill="#fff">
        <path d="M9 7 l4 0 l1 5 l-2 2 q2 4 5 5 l2 -2 l5 1 l0 4 q-12 1 -15 -15z"/>
        <path d="M37 15 l10 -9 l10 9 h-3 v8 h-5 v-5 h-4 v5 h-5 v-8z"/>
        <text x="80" y="21" text-anchor="middle" font-family="Arimo, sans-serif" font-size="18">@</text>
        <path d="M104 14 h4 v10 h-4z M109 14 l4 -7 q3 0 2 4 l-1 3 h6 q2 1 1 3 l-2 6 q-1 1 -3 1 h-7z"/>
        <rect x="139" y="9" width="16" height="12" rx="1"/>
        <path d="M139 9 l8 7 l8 -7" fill="none" stroke="var(--teal)" stroke-width="1.5"/>
        <path d="M172 8 h16 v10 h-8 l-5 4 v-4 h-3z"/>
      </g>
    </svg>

    <footer class="site-footer">
      <div class="col legal">Coral Pillow Depot inc.<br>All right reserved<br>www.coralpillowdepot.com</div>
      <div class="col social">Social media<br>http://circlebook.net/coralpillowdepot<br>http://chirpline.net/coralpillowdepot</div>
      <div class="col helpline">For more information please call our helpline at:(786)555-0147</div>
      <div class="thumb" role="img" aria-label="Mattress thumbnail" style="left:637px;width:73px"></div>
      <div class="thumb" role="img" aria-label="Mattress thumbnail" style="left:716px;width:72px"></div>
      <div class="thumb" role="img" aria-label="Mattress thumbnail" style="left:793px;width:72px"></div>
      <div class="thumb" role="img" aria-label="Mattress thumbnail" style="left:872px;width:72px"></div>
    </footer>
  </div>
</body>
</html>
```